The Book Cover for "Finding the Silver Lantern of Dawn" needs redesigned

First the back ground or art work needs to be replaced or redesigned.
The title Finding the Silver Lantern of Dawn needs to be redesigned so that the words "Finding the" is diminished in size compared to the rest of the title "Silver Lantern of Dawn"
The Sub-title "Tracing the forgotten path of the Evening Wind" needs to be more pronounced and readable.
The authors name needs to be downsized.

```html
<!DOCTYPE html>
<html lang="en">
<head>
<meta charset="utf-8">
<title>Finding the Silver Lantern of Dawn — Book Cover</title>
<link rel="stylesheet" href="https://fonts.googleapis.com/css2?family=Montserrat:wght@600;700;800&family=Playfair+Display:wght@600&family=Uncial+Antiqua&display=swap">
<style>
  :root {
    --sky-top: #2b0c16;
    --sky-mid: #7a2430;
    --glow: #f08a3c;
    --glow-core: #ffd27a;
    --sea: #1b2436;
    --ink-white: #ffffff;
    --title-rose: #f4a08c;
    --subtitle-teal: #3fdccb;
    --author-rose: #f2b9aa;
  }
  * { box-sizing: border-box; margin: 0; padding: 0; }
  html, body {
    width: 889px;
    height: 1200px;
    overflow: hidden;
    background: var(--sky-top);
  }
  .book-cover {
    position: relative;
    width: 889px;
    height: 1200px;
    overflow: hidden;
    text-align: center;
    color: var(--ink-white);
  }
  .cover-art {
    position: absolute;
    inset: 0;
    background:
      radial-gradient(ellipse 38% 16% at 50% 60%, var(--glow-core) 0%, rgba(240,138,60,0.85) 35%, rgba(240,138,60,0) 100%),
      radial-gradient(ellipse 80% 40% at 50% 58%, rgba(230,110,60,0.75) 0%, rgba(122,36,48,0) 70%),
      linear-gradient(180deg, var(--sky-top) 0%, var(--sky-mid) 30%, #c0503a 52%, #8c3a3a 64%, #3a2a3c 78%, var(--sea) 100%);
  }
  .cover-art::after {
    content: "";
    position: absolute;
    inset: 0;
    background: radial-gradient(ellipse 75% 65% at 50% 55%, rgba(0,0,0,0) 55%, rgba(10,4,10,0.55) 100%);
  }
  .figures-silhouette {
    position: absolute;
    left: 285px;
    top: 560px;
    width: 320px;
    height: 480px;
    background: linear-gradient(180deg, rgba(70,26,34,0.85) 0%, rgba(40,24,40,0.9) 100%);
    border-radius: 45% 45% 8% 8% / 22% 22% 4% 4%;
    filter: blur(2px);
  }
  .title-block {
    position: absolute;
    top: 82px;
    left: 0;
    right: 0;
  }
  .title-lead {
    font-family: "Montserrat", sans-serif;
    font-weight: 800;
    font-size: 40px;
    letter-spacing: 4px;
    color: var(--ink-white);
  }
  .title-main {
    margin-top: 14px;
    font-family: "Playfair Display", serif;
    font-weight: 600;
    font-size: 84px;
    line-height: 1;
    letter-spacing: 1px;
    text-transform: uppercase;
    color: var(--title-rose);
  }
  .title-tail {
    margin-top: 6px;
    font-family: "Uncial Antiqua", serif;
    font-size: 88px;
    line-height: 1.1;
    color: var(--ink-white);
  }
  .subtitle {
    position: absolute;
    top: 948px;
    left: 0;
    right: 0;
    font-family: "Montserrat", sans-serif;
    font-weight: 800;
    font-size: 38px;
    line-height: 1.25;
    letter-spacing: 1px;
    text-transform: uppercase;
  }
  .subtitle-accent { display: block; color: var(--subtitle-teal); }
  .subtitle-rest { display: block; color: var(--ink-white); }
  .author {
    position: absolute;
    top: 1112px;
    left: 0;
    right: 0;
    font-family: "Montserrat", sans-serif;
    font-weight: 600;
    font-size: 26px;
    letter-spacing: 4px;
    text-transform: uppercase;
    color: var(--author-rose);
  }
</style>
</head>
<body>
  <main class="book-cover">
    <div class="cover-art" role="img" aria-label="Sunset over calm water with a glowing sun on the horizon and a mother holding a small child, seen from behind, silhouetted against the light">
      <div class="figures-silhouette"></div>
    </div>

    <h1 class="title-block">
      <span class="title-lead">FINDING THE</span>
      <div class="title-main">Silver Lantern</div>
      <div class="title-tail">of Dawn</div>
    </h1>

    <p class="subtitle">
      <span class="subtitle-accent">Tracing the forgotten path</span>
      <span class="subtitle-rest">of the Evening Wind</span>
    </p>

    <p class="author">R T Hollis Wrenfield</p>
  </main>
</body>
</html>
```